Dan Brackley - award winning wildlife filmmaker and photographer

We need a web site which we can access and update ourselves, should have the following pages : home; about me; gallery - with pictures so that people can also buy them online placing an order with us; video clip page; contact page; blog page.
Image is very much 'Rexford Callowish', rough rugged but distinguished, mature, very close to nature (walks around barefoot), african feel to it. Leatherbound book with handstitching - perhaps an old looking photo album leatherbound with black triangles around corners of pictures. Perhaps a sepia feel to it with sepia pics of Dan but then the gallery pics are in colour. Natural colours. Please check out this template which we loved but need someone to adjust it to our needs http://www.sitepattern-example.com/website-templates/839104556-QX00417/#brown - in fact I purchased the template but don't have enough design skills or the programme to change it to how we would like - if you want I can send the files and you can adjust it to what we need? it would probably save time - or if you have something similar but better we can take a look. I have tons more pictures to upload but have uploaded a few to give you a feel.

Target Market(s)

Animal lovers, conservation, wildlife, photographers, filmmaking, outdoor enthusiasts, women, men, all ages

Industry/Entity Type

Online

Requirements
Must have
• WE REALLY LOVED THIS TEMPLATE (its the only one we have come across which projects the right image) - http://www.sitepattern-example.com/website-templates/839104556-QX00417/#brown - if you could make it similar(or identical) with a few changes. We want a slide show instead of all the pics at once ?? I did purchase the template and can send you the files to play around with??
Easy to use after initial design has been done - ie want to be able to access it ourselves and make necessary changes ie. blog, gallery, photos, links etc
Full page photos
Social network
Masculine
Traditional (in an African way)
Leatherbound (see above design)
Our logo which is Tokoni Media (see attached)
Gallery with pricing page (maybe separate) - appox 20 pics - which can be updated and changed by ourselves when needed
About page
Blog page which can be accessed and managed by us
Video clip page

```html
<!DOCTYPE html>
<html lang="en">
<head>
<meta charset="utf-8">
<title>Tokoni Media – Dan Brackley</title>
<link href="https://fonts.googleapis.com/css2?family=Arimo:wght@400;700&display=swap" rel="stylesheet">
<style>
:root{
  --leather:#c4702e;
  --leather-dark:#8f4a1c;
  --leather-light:#d88a45;
  --panel:rgba(60,25,10,0.55);
  --text:#ffffff;
  --gold:#e8b24a;
  --strip:#e4c3a6;
  --olive:#5f5a2b;
  --arrow:#d01f1f;
  --sepia-a:#3a2f26;
  --sepia-b:#a89480;
}
*{margin:0;padding:0;box-sizing:border-box}
html,body{width:1200px;height:1070px;overflow:hidden}
body{
  font-family:"Arimo",Arial,sans-serif;color:var(--text);position:relative;
  background:radial-gradient(ellipse at 70% 20%,var(--leather-light),var(--leather) 45%,var(--leather-dark) 100%);
}
.abs{position:absolute}
.intro-panel{left:12px;top:0;width:384px;height:686px;background:var(--panel)}
.intro-title{left:38px;top:67px;font-size:18px;font-weight:700}
.intro-copy{left:38px;top:102px;width:332px;font-size:16px;line-height:17.9px;text-align:justify}
.intro-copy p{margin-bottom:17.9px}
.brand{left:600px;top:140px;width:372px;text-align:center;font-size:34px;letter-spacing:8px;color:#f3eadf}
.brand-mark{left:728px;top:28px;width:112px;height:100px;background:#6b6434}
.main-nav{left:423px;top:222px;font-size:19px;font-weight:700;word-spacing:2px;white-space:nowrap}
.main-nav span{margin:0 20px}
.main-nav span:first-child{margin-left:0}
.hero-frame{left:405px;top:267px;width:748px;height:414px;border:4px solid var(--gold);border-radius:30px;overflow:hidden}
.hero-photo{width:100%;height:100%;background:linear-gradient(100deg,var(--sepia-a) 0%,#6e5e50 45%,var(--sepia-b) 100%)}
.gallery-band{left:0;top:693px;width:1200px;height:182px;background:var(--strip);opacity:0.85}
.slide-btn{top:708px;width:58px;height:147px;background:#fff}
.slide-prev{left:0}
.slide-next{left:1144px;width:56px}
.thumb{top:710px;height:145px}
.footer-social{font-size:13px;line-height:16px;white-space:nowrap}
.social-icon{width:34px;height:34px;background:#f2e8dc;border-radius:4px}
.footer-nav{left:683px;top:910px;font-size:12.5px;font-weight:700;white-space:nowrap}
.footer-nav span{margin:0 13px}
.footer-nav span:first-child{margin-left:0}
.footer-brand{left:838px;top:1003px;width:172px;text-align:center;font-size:17px;letter-spacing:4px;color:#f3eadf}
.footer-mark{left:895px;top:948px;width:50px;height:48px;background:#6b6434}
.base-bar{left:0;top:1046px;width:1200px;height:24px;background:var(--olive)}
</style>
</head>
<body>
<div class="abs intro-panel"></div>
<h1 class="abs intro-title">IT’S NOT ABOUT THE CAMERA………</h1>
<div class="abs intro-copy">
  <p>IT’S ABOUT THE LIFESTYLE and cameras provide me with the challenge to bring home stunning images and footage which help to pay my way, so allowing me to live this idyllic lifestyle.<br>I spend many months in the field getting very intimate with my film subjects until they totally ignore me and behave in the most natural way as if I wasn’t there. It goes beyond that too – they grant me the absolute honour and privilege to become a part of their lives. Now that’s the big Wow!<br>Life doesn’t get much better than this.</p>
  <p>I’ve had the good fortune of developing these very intimate bonds with African Wild Dogs, Leopard, Cheetah and Spotted Hyaenas.</p>
  <p>I live on location and spend many months in the field getting very intimate with my film subjects. It finally gets to a stage where they totally ignore me and behave in the most natural way as if I wasn’t there.</p>
  <p>I get very intimate with my subjects, spending months with them until they totally ignore me and go about their behavior in a most natural way as if I wasn’t there. It goes beyond that – they grant me the honour and privilege to become a part of their lives.</p>
</div>

<div class="abs brand-mark"></div>
<div class="abs brand">TOKONI MEDIA</div>

<nav class="abs main-nav"><span>HOME</span>|<span>ABOUT US</span>|<span>SERVICES</span>|<span>PHOTO GALLERY</span>|<span>CONTACT US</span></nav>

<div class="abs hero-frame"><div class="hero-photo" role="img" aria-label="Sepia portrait of the filmmaker in a brimmed hat behind a professional video camera"></div></div>

<div class="abs gallery-band"></div>
<div class="abs slide-btn slide-prev"><svg width="58" height="147" viewBox="0 0 58 147"><polygon points="4,75 22,60 22,68 48,68 48,82 22,82 22,90" fill="var(--arrow)"/></svg></div>
<div class="abs slide-btn slide-next"><svg width="56" height="147" viewBox="0 0 56 147"><polygon points="52,75 34,60 34,68 8,68 8,82 34,82 34,90" fill="var(--arrow)"/></svg></div>
<div class="abs thumb" style="left:71px;width:177px;background:linear-gradient(#7d8a6a,#5e5a5c)" role="img" aria-label="Rhino standing in grassland"></div>
<div class="abs thumb" style="left:261px;width:196px;background:linear-gradient(#6f9a3c,#a77a4c)" role="img" aria-label="Group of impala"></div>
<div class="abs thumb" style="left:471px;width:191px;background:linear-gradient(#8fb050,#5d8a2c)" role="img" aria-label="Secretary bird walking in grass"></div>
<div class="abs thumb" style="left:675px;width:219px;background:linear-gradient(#6a8a3a,#b59a68)" role="img" aria-label="Cheetah cub among flowers"></div>
<div class="abs thumb" style="left:906px;width:227px;background:linear-gradient(#b8a48a,#6d5d4c)" role="img" aria-label="Sepia photo of an elephant near a vehicle at a waterhole"></div>

<div class="abs footer-social" style="left:25px;top:884px"><div class="social-icon"></div></div>
<div class="abs footer-social" style="left:70px;top:884px">PIXFOLIO<br>http://www.pixfolio-example.com/photos/wildreel/</div>
<div class="abs footer-social" style="left:25px;top:934px"><div class="social-icon"></div></div>
<div class="abs footer-social" style="left:70px;top:934px">CLIPSTREAM<br>http://www.clipstream-example.com/user/wildreelr</div>
<div class="abs footer-social" style="left:25px;top:984px"><div class="social-icon"></div></div>
<div class="abs footer-social" style="left:70px;top:984px">FRIENDWALL<br>http://www.friendwall-example.com/dan.brackley?ref=ts</div>
<div class="abs footer-social" style="left:406px;top:884px"><div class="social-icon"></div></div>
<div class="abs footer-social" style="left:451px;top:884px">CHIRPLINE<br>https://chirpline.net/danbrackley</div>
<div class="abs footer-social" style="left:451px;top:936px">WILDREEL<br>http://www.wildreel-example.net/</div>

<nav class="abs footer-nav"><span>HOME</span>|<span>ABOUT US</span>|<span>SERVICES</span>|<span>PHOTO GALLERY</span>|<span>CONTACT US</span></nav>
<div class="abs footer-mark"></div>
<div class="abs footer-brand">TOKONI MEDIA</div>

<div class="abs base-bar"></div>
</body>
</html>
```